Criação de Papelaria Profissional para Crianças & Infantil
A empresa queria:
" Esta empresa preza por vender roupas de altíssima qualidade e marcas diferenciadas, a fim de encantar pais e filhos, garantindo conforto e estilo aos pequenos. "

```html
<!DOCTYPE html>
<html lang="pt-BR">
<head>
<meta charset="UTF-8">
<title>Cartão de Visita – Lumibê</title>
<link href="https://fonts.googleapis.com/css2?family=Nunito:wght@600;700;800;900&display=swap" rel="stylesheet">
<style>
  :root{
    --bg:#e7e7e9;
    --bg-shade:#d5d5d8;
    --purple:#6a2a8c;
    --purple-ink:#5b2a86;
    --white:#ffffff;
    --text:#4a3a5a;
    --mint:#8fd8c6;
    --yellow:#f3c14b;
    --pink:#ef8f91;
    --blue:#8cc8ec;
    --icon:#f0b54a;
  }
  *{box-sizing:border-box;margin:0;padding:0}
  html,body{width:1200px;height:1200px;overflow:hidden}
  body{font-family:"Nunito",sans-serif;background:var(--bg);position:relative}
  .backdrop{position:absolute;inset:0}
  .sheet-title{
    position:absolute;top:48px;left:0;width:1200px;text-align:center;
    font-weight:900;font-size:34px;letter-spacing:5px;color:var(--purple-ink);
  }
  .card{
    position:absolute;left:233px;width:734px;height:432px;border-radius:24px;overflow:hidden;
    box-shadow:0 4px 14px rgba(0,0,0,.12);
  }
  .card--front{top:151px;background:var(--purple)}
  .card--back{top:631px;height:425px;background:var(--white)}
  .stripes{position:absolute;left:0;bottom:0;width:100%;height:30px;display:flex}
  .stripes span{height:100%}
  .s-mint{background:var(--mint);width:151px}
  .s-yellow{background:var(--yellow);width:216px}
  .s-pink{background:var(--pink);width:216px}
  .s-blue{background:var(--blue);flex:1}

  .brand{position:absolute;left:150px;top:150px;display:flex;align-items:center;gap:22px}
  .brand-dot{width:64px;height:64px;border-radius:50%;background:var(--white)}
  .brand-name{font-weight:900;font-size:104px;line-height:1;color:var(--white)}
  .tagline{position:absolute;right:152px;top:266px;font-weight:800;font-size:22px;color:var(--white);white-space:nowrap}

  .contact{position:absolute;left:50px;top:60px;color:var(--text)}
  .person{font-weight:800;font-size:27px;color:var(--purple-ink)}
  .role{font-weight:600;font-size:20px;color:var(--purple-ink);margin-top:6px}
  .line{display:flex;align-items:flex-start;gap:10px;font-weight:600;font-size:19px;line-height:24px}
  .line svg{flex:none;margin-top:2px}
  .phones{margin-top:20px}
  .address{margin-top:12px}
  .email{margin-top:10px}
  .social{margin-top:20px}
  .dot{width:18px;height:18px;border-radius:50%;border:2.5px solid var(--icon);flex:none;margin-top:3px}
  .decor{position:absolute;left:400px;top:30px;width:320px;height:360px;border-radius:30px;
    background:radial-gradient(circle at 55% 45%, rgba(180,135,207,.35), rgba(140,200,236,.12) 60%, rgba(255,255,255,0) 75%)}
</style>
</head>
<body>
  <svg class="backdrop" width="1200" height="1200" viewBox="0 0 1200 1200" aria-hidden="true">
    <polygon points="0,1200 1200,160 1200,1200" fill="var(--bg-shade)"/>
  </svg>

  <h1 class="sheet-title">CARTÃO DE VISITA</h1>

  <section class="card card--front">
    <div class="brand">
      <span class="brand-dot"></span>
      <span class="brand-name">Lumibê</span>
    </div>
    <p class="tagline">Carinho que veste e encanta</p>
    <div class="stripes"><span class="s-mint"></span><span class="s-yellow"></span><span class="s-pink"></span><span class="s-blue"></span></div>
  </section>

  <section class="card card--back">
    <div class="decor" role="img" aria-label="Área decorativa com o símbolo da marca e estrelas coloridas"></div>
    <div class="contact">
      <p class="person">Nome e Sobrenome</p>
      <p class="role">Diretor Comercial</p>
      <div class="line phones">
        <svg width="18" height="20" viewBox="0 0 24 24"><path d="M6.6 10.8a15 15 0 0 0 6.6 6.6l2.2-2.2a1 1 0 0 1 1-.25 11 11 0 0 0 3.6.6 1 1 0 0 1 1 1V20a1 1 0 0 1-1 1A17 17 0 0 1 3 4a1 1 0 0 1 1-1h3.5a1 1 0 0 1 1 1 11 11 0 0 0 .6 3.6 1 1 0 0 1-.25 1z" fill="none" stroke="var(--icon)" stroke-width="2"/></svg>
        <span>(99) 90312-5578<br>(99) 90487-2260</span>
      </div>
      <div class="line address">
        <svg width="18" height="22" viewBox="0 0 24 28"><path d="M12 26s-8-8.5-8-14a8 8 0 0 1 16 0c0 5.5-8 14-8 14z" fill="none" stroke="var(--icon)" stroke-width="2.2"/><circle cx="12" cy="12" r="3" fill="var(--icon)"/></svg>
        <span>Rua das Acácias, 380 - Centro<br>Cidade/UF - CEP: 12345-678</span>
      </div>
      <div class="line email">
        <svg width="18" height="20" viewBox="0 0 24 24"><rect x="2" y="5" width="20" height="14" rx="2" fill="none" stroke="var(--icon)" stroke-width="2"/><path d="M2.5 6l9.5 7 9.5-7" fill="none" stroke="var(--icon)" stroke-width="2"/></svg>
        <span>lumibe@mail.com</span>
      </div>
      <div class="line social">
        <span class="dot"></span>
        <span>@lumibe</span>
      </div>
    </div>
    <div class="stripes"><span class="s-mint"></span><span class="s-yellow"></span><span class="s-pink"></span><span class="s-blue"></span></div>
  </section>
</body>
</html>
```